Collectible Card Trading Company ~ Fern and Quill Keepsakes

Business card design using the attached images as a reference point. The color pallet is the color choice I prefer. If you have any way of improving on the design that would be appreciated. This will be used as an insert for product shipments as well as at vexafest and other collectible trade shows so it needs to be eye catching and memorable. Anything that you can do to make my business POP with this business card would be appreciated.

Target Market(s)

Collectible card purchasers primarily but all collectors ingeneral

Industry/Entity Type

Retail

Contact Information for Business Card

Details are included on the provided images

Colors

Designer to choose colors to be used in the design.

Requirements
Must have
• Bold design
Nice to have
• N/A
Should not have
• N/A

```html
<!DOCTYPE html>
<html lang="en">
<head>
<meta charset="utf-8">
<title>Fern &amp; Quill Co. — Business Card</title>
<link href="https://fonts.googleapis.com/css2?family=Lora:wght@400;700&family=Oswald:wght@300;500;600&family=Saira:wght@400&display=swap" rel="stylesheet">
<style>
  :root {
    --bg: #e2dede;
    --copper-light: #b8672a;
    --copper: #a4561f;
    --copper-dark: #7e3c14;
    --slate-light: #4a5867;
    --slate: #3a4552;
    --slate-dark: #2a323c;
    --gold: #c58a45;
    --paper-white: #f4ece4;
  }
  * { margin: 0; padding: 0; box-sizing: border-box; }
  html, body { width: 1200px; height: 1200px; overflow: hidden; background: var(--bg); }
  .canvas {
    width: 1200px; height: 1200px;
    display: flex; flex-direction: column; align-items: center; justify-content: center;
    gap: 60px;
  }
  .card {
    position: relative;
    width: 840px; height: 480px;
    border-radius: 4px;
    box-shadow: 0 18px 36px rgba(0,0,0,.18);
    overflow: hidden;
  }

  /* Back side: contact details */
  .card--back {
    background: radial-gradient(ellipse at 60% 30%, var(--copper-light), var(--copper) 55%, var(--copper-dark));
    color: var(--paper-white);
  }
  .holder {
    position: absolute; left: 50%; top: 44%;
    transform: translate(-50%, -50%);
    font-family: "Lora", serif; font-weight: 700;
    font-size: 34px; line-height: 1.1; text-align: center; white-space: nowrap;
  }
  .edge { position: absolute; font-family: "Lora", serif; font-size: 20px; white-space: nowrap; }
  .edge--top { top: 18px; left: 50%; transform: translateX(-50%) rotate(180deg); }
  .edge--right { right: 14px; top: 50%; transform: translate(50%, -50%) rotate(90deg) translateY(-50%); }
  .edge--left {
    left: 28px; top: 50%;
    transform: translate(-50%, -50%) rotate(90deg);
    text-align: center; line-height: 1.35;
  }
  .edge--left .handle-strong { font-family: "Oswald", sans-serif; font-weight: 600; }
  .contact {
    position: absolute; right: 110px; bottom: 48px;
    font-family: "Oswald", sans-serif; font-weight: 300;
    font-size: 26px; line-height: 1.25; text-align: center; white-space: nowrap;
  }

  /* Front side: company name */
  .card--front {
    background: radial-gradient(ellipse at 40% 35%, var(--slate-light), var(--slate) 55%, var(--slate-dark));
    color: var(--gold);
  }
  .brand {
    position: absolute; left: 0; right: 0; top: 40px;
    text-align: center;
    font-family: "Oswald", sans-serif; font-weight: 500; font-size: 76px; line-height: 1; white-space: nowrap;
  }
  .emblem-area {
    position: absolute; left: 305px; top: 150px;
    width: 230px; height: 210px; border-radius: 8px;
    background: radial-gradient(circle, rgba(197,138,69,.38), rgba(197,138,69,.08));
  }
  .est { position: absolute; font-family: "Lora", serif; font-size: 28px; line-height: 1; }
  .est--label { left: 232px; top: 326px; }
  .est--year { left: 556px; top: 200px; }
  .tagline {
    position: absolute; left: 0; right: 0; top: 386px;
    text-align: center;
    font-family: "Saira", sans-serif; font-size: 36px; line-height: 1; letter-spacing: 1px; white-space: nowrap;
  }
</style>
</head>
<body>
<main class="canvas">
  <section class="card card--back" aria-label="Card back with contact details">
    <p class="edge edge--top">shop@www.tradeloft.com/str/fernandquillco</p>
    <p class="edge edge--right">www.fernandquillco.com</p>
    <p class="edge edge--left">snapfeed@fernandquillco<br><span class="handle-strong">chirper@Fern_and_Quill</span></p>
    <h2 class="holder">milo archer jr.<br>chief collector</h2>
    <p class="contact">milo@fernandquillco.com<br>alder springs, colorado</p>
  </section>

  <section class="card card--front" aria-label="Card front with company name">
    <h1 class="brand">Fern &amp; Quill Co.</h1>
    <div class="emblem-area" role="img" aria-label="Area for the company emblem artwork"></div>
    <p class="est est--label">est.</p>
    <p class="est est--year">2016</p>
    <p class="tagline">Cards &amp; Collectibles</p>
  </section>
</main>
</body>
</html>
```